Business Cards Needed For Veterinary Business

Looking for a business card design for a veterinary blood bank. We would like it to be clean and professional on appearance but still warm and inviting. We would like to utilize our logo and similar coloring. We will use our phone number, email, website, employee name, employee title.

We do not want a bunch of animated animal photos but do not need the style to be as clinical as a laboratory or human medical procedure office.

We are looking for some creative ideas to choose from so that we can generate a standout professional business card for our management team to utilize.

Target Market(s)

professionals

Industry/Entity Type

veterinary

Contact Information for Business Card

employee name, employee title, phone number, website URL, email

Font styles to use
Sans Serif

Colors
0054AA
0677BA
7BADD7
CADEEF
E8F1F8
EB3D1F
EC4F4E
F09395
F8D3D4
FCEDEE

Requirements
Nice to have
• creative design
Should not have
• animated photos

```html
<!DOCTYPE html>
<html lang="en">
<head>
<meta charset="utf-8">
<title>Harbor Veterinary Blood Bank – Business Card</title>
<link href="https://fonts.googleapis.com/css2?family=Montserrat:wght@400;500;700;800&display=swap" rel="stylesheet">
<style>
  :root {
    --stage: #262728;
    --card: #ffffff;
    --card-edge: #f1f1f1;
    --brand-red: #eb3d1f;
    --band-red: #e4232b;
    --brand-blue: #0054aa;
    --text-grey: #3c3c3c;
    --silhouette: #6b6c70;
  }
  * { box-sizing: border-box; margin: 0; padding: 0; }
  html, body {
    width: 1200px; height: 1200px; overflow: hidden;
    background: var(--stage);
    font-family: "Montserrat", sans-serif;
  }
  .sheet {
    width: 1200px; height: 1200px;
    display: flex; flex-direction: column; align-items: center; justify-content: center;
    gap: 56px;
  }
  .card {
    position: relative;
    width: 900px; height: 514px;
    background: linear-gradient(135deg, var(--card) 60%, var(--card-edge));
    border-radius: 34px;
    overflow: hidden;
  }

  /* Brand lockup (name set as text) */
  .brand {
    display: flex; align-items: center; gap: 18px;
    color: var(--brand-red);
    font-weight: 800;
  }
  .brand-dot {
    flex: none;
    border-radius: 50%;
    background: var(--brand-red);
  }
  .brand-name { line-height: 1.05; text-transform: uppercase; }

  /* Front */
  .card-front .brand { position: absolute; left: 56px; top: 196px; }
  .card-front .brand-dot { width: 58px; height: 58px; }
  .card-front .brand-name { font-size: 30px; }

  .identity {
    position: absolute; right: 70px; top: 70px; text-align: right;
  }
  .identity-name {
    color: var(--brand-blue); font-weight: 700; font-size: 36px; line-height: 1.1;
  }
  .identity-title {
    color: var(--text-grey); font-weight: 500; font-size: 22px; margin-top: 4px; margin-right: 6px;
  }

  .contacts {
    position: absolute; right: 54px; top: 218px;
    list-style: none; text-align: right;
  }
  .contacts li {
    display: flex; align-items: center; justify-content: flex-end; gap: 14px;
    color: var(--text-grey); font-size: 21px; font-weight: 500;
    height: 40px;
  }
  .contacts svg { width: 20px; height: 20px; fill: var(--brand-blue); }
  .contacts li.web svg { fill: var(--band-red); }

  .web-band {
    position: absolute; left: 390px; right: 0; top: 352px; height: 44px;
    background: var(--band-red);
    display: flex; align-items: center; justify-content: flex-end;
    padding-right: 88px;
    color: #ffffff; font-weight: 700; font-size: 21px; letter-spacing: 0.3px;
  }

  .pets-art {
    position: absolute; left: 190px; bottom: 0;
    width: 210px; height: 200px;
    background: var(--silhouette);
    border-radius: 90px 90px 0 0;
  }

  /* Back */
  .card-back { display: flex; align-items: center; justify-content: center; }
  .card-back .brand { gap: 26px; }
  .card-back .brand-dot { width: 96px; height: 96px; }
  .card-back .brand-name { font-size: 46px; }
</style>
</head>
<body>
<main class="sheet">

  <section class="card card-front" aria-label="Business card front">
    <div class="brand">
      <span class="brand-dot"></span>
      <span class="brand-name">Harbor Veterinary<br>Blood Bank</span>
    </div>

    <div class="identity">
      <p class="identity-name">Your Name</p>
      <p class="identity-title">Designation</p>
    </div>

    <ul class="contacts">
      <li class="phone">1234 567890
        <svg viewBox="0 0 24 24" aria-hidden="true"><path d="M6.6 10.8a15.1 15.1 0 0 0 6.6 6.6l2.2-2.2c.3-.3.7-.4 1-.2 1.1.4 2.3.6 3.6.6.6 0 1 .4 1 1V20c0 .6-.4 1-1 1A17 17 0 0 1 3 4c0-.6.4-1 1-1h3.5c.6 0 1 .4 1 1 0 1.3.2 2.5.6 3.6.1.3 0 .7-.2 1z"/></svg>
      </li>
      <li class="mail">harborvbb.com
        <svg viewBox="0 0 24 24" aria-hidden="true"><path d="M3 5h18v14H3z M3 5l9 7 9-7" stroke="#fff" stroke-width="1.6"/></svg>
      </li>
      <li class="web">info@harborvbb.com
        <svg viewBox="0 0 24 24" aria-hidden="true"><circle cx="12" cy="12" r="10"/><path d="M2 12h20M12 2c3 3 3 17 0 20M12 2c-3 3-3 17 0 20" stroke="#fff" stroke-width="1.4" fill="none"/></svg>
      </li>
    </ul>

    <div class="web-band">www.harborvbb.com</div>

    <div class="pets-art" role="img" aria-label="Grey silhouette of a dog and a cat sitting together"></div>
  </section>

  <section class="card card-back" aria-label="Business card back">
    <div class="brand">
      <span class="brand-dot"></span>
      <span class="brand-name">Harbor Veterinary<br>Blood Bank</span>
    </div>
  </section>

</main>
</body>
</html>
```